Engineering Consultant Business Card

I'm starting a new business as a high-end engineering consultant in a niche field. I've attached the jpg for my logo plus the branding guideline document that I've been following. You can see my business website here: www.orvalink.com
I'd like a business card that has the logo on one side, then the other side has (in any order): Tessmor Pact, Inc.
Delia Whitcombe
President and Chief EMC Engineer
www.orvalink.com
delia@orvalink.com
Optional: motto "We will solve your EMC problems as early as possible—ideally before they even start."
I'm not planning on including a phone number
Target Market(s)
Businesses, especially makers of electronics hardware
Industry/Entity Type
Electrical engineering
Contact Information for Business Card
Company name, my name, website, email
Look and feel
Each slider illustrates characteristics of the customer's brand and the style your logo design should communicate.

```html
<!DOCTYPE html>
<html lang="en">
<head>
<meta charset="utf-8">
<title>Tessmor Pact — Business Card</title>
<link rel="stylesheet" href="https://fonts.googleapis.com/css2?family=Archivo:wght@400;500;700;800&display=swap">
<style>
  :root {
    --brand-blue: #2841a0;
    --brand-blue-deep: #233a94;
    --card-white: #f6f6f6;
    --ink: #1b1b22;
    --stage: #2a2a2c;
  }
  * { box-sizing: border-box; margin: 0; padding: 0; }
  html, body {
    width: 1200px; height: 1107px; overflow: hidden;
    background: var(--stage);
    font-family: "Archivo", Arial, sans-serif;
  }
  .stage {
    position: relative; width: 1200px; height: 1107px;
    display: flex; justify-content: center; align-items: center; gap: 70px;
  }
  .card {
    position: relative; width: 380px; height: 664px;
    border-radius: 22px; overflow: hidden;
  }
  .card--front { background: var(--card-white); }
  .card--back { background: var(--brand-blue-deep); }

  .brand-mark {
    display: flex; align-items: center; justify-content: center; gap: 14px;
  }
  .brand-mark__dot {
    width: 34px; height: 34px; border-radius: 50%;
    background: currentColor;
  }
  .brand-mark__name {
    font-weight: 800; font-size: 40px; letter-spacing: 0.5px; line-height: 1;
  }
  .card--front .brand-mark { color: var(--brand-blue); margin-top: 120px; }

  .identity { text-align: center; margin-top: 100px; }
  .identity__name {
    color: var(--brand-blue); font-weight: 800; font-size: 27px;
    letter-spacing: 0.5px; text-transform: uppercase;
  }
  .identity__title {
    color: var(--ink); font-size: 16px; margin-top: 6px; font-weight: 500;
  }
  .contact { text-align: center; margin-top: 26px; color: var(--ink); }
  .contact__icons { display: flex; justify-content: center; gap: 10px; margin-bottom: 10px; }
  .contact__line { font-size: 17px; line-height: 1.4; letter-spacing: 0.3px; }

  .motto-band {
    position: absolute; left: 0; right: 0; bottom: 0; height: 132px;
    background: var(--brand-blue);
    color: #fff; display: flex; align-items: center;
    padding: 0 30px; font-size: 15px; font-weight: 500; line-height: 1.45;
  }

  .back-texture {
    position: absolute; inset: 0;
    background: linear-gradient(160deg, #2c47a8 0%, #243c98 55%, #2a44a4 100%);
  }
  .card--back .brand-mark {
    position: absolute; left: 0; right: 0; bottom: 120px; color: #fff;
  }
</style>
</head>
<body>
<main class="stage">
  <section class="card card--front" aria-label="Business card front">
    <div class="brand-mark">
      <span class="brand-mark__dot"></span>
      <span class="brand-mark__name">Tessmor Pact</span>
    </div>
    <div class="identity">
      <h1 class="identity__name">Delia Whitcombe</h1>
      <p class="identity__title">President and Chief EMC Engineer</p>
    </div>
    <div class="contact">
      <div class="contact__icons">
        <svg width="18" height="14" viewBox="0 0 18 14" aria-hidden="true">
          <rect x="0.5" y="0.5" width="17" height="13" fill="var(--brand-blue)"/>
          <path d="M1 1 L9 8 L17 1" fill="none" stroke="#fff" stroke-width="1.3"/>
        </svg>
        <svg width="15" height="15" viewBox="0 0 16 16" aria-hidden="true">
          <circle cx="8" cy="8" r="7" fill="none" stroke="var(--brand-blue)" stroke-width="1.5"/>
          <ellipse cx="8" cy="8" rx="3" ry="7" fill="none" stroke="var(--brand-blue)" stroke-width="1.2"/>
          <line x1="1" y1="8" x2="15" y2="8" stroke="var(--brand-blue)" stroke-width="1.2"/>
        </svg>
      </div>
      <p class="contact__line">delia@orvalink.com</p>
      <p class="contact__line">www.orvalink.com</p>
    </div>
    <div class="motto-band">
      <p>We will solve your EMC problems as early as possible—ideally before they even start.</p>
    </div>
  </section>

  <section class="card card--back" aria-label="Business card back">
    <div class="back-texture" role="img" aria-label="Embossed repeating brand pattern in tonal blue"></div>
    <div class="brand-mark">
      <span class="brand-mark__dot"></span>
      <span class="brand-mark__name">Tessmor Pact</span>
    </div>
  </section>
</main>
</body>
</html>
```